International Supplier needs an eye catching profssional letterhead and continuation page

We need a letterhead and continuation sheet designed for a company based in Austria called VULMA Screens GmbH. We develop and install innovate glass partition wall solutions to commercial and cultural buildings and to some of the most contemporary architectural buildings in Europe. I have our inhouse design brief confirming our corporate colours, fonts and images and have our corporate logo available in a variety of formats including AI and EPS. We are open to differing design suggestions as long as they follow the colour and font specification in our corporate design brief. We are at the forefront of innovation, craftmanship and design for architectural glass, framing systems and fire rated partition systems. The final design should communicate the spirit and strength of the company.
www.vulma.com / www.parvoline.co.uk / www.emberpane.com

Target Market(s)

Architects, planners, designers, building contractors and construction companies

Industry/Entity Type

Architecture

Font styles to use
Sans Serif

Requirements
Must have
• VULMA Screens GmbH
• Lindorferweg 14 B
• 7410 Hollendorf
• Österreich
• Tel: +43 (1) 482 6170
• E-mail:office@vulmascreens.at
• Web:www.vulmascreens.at / www.vulmaemberpane.com
• subtle yet professionally distinctive
• colours and fonts to be taken ffom VULMA design guide but we are also open to variations on the same theme
Should not have
• No bold lines

```html
<!DOCTYPE html>
<html lang="de">
<head>
<meta charset="utf-8">
<title>VULMA Screens GmbH – Briefpapier</title>
<link href="https://fonts.googleapis.com/css2?family=Questrial&display=swap" rel="stylesheet">
<style>
  :root {
    --brand-red: #bb1239;
    --ink: #1c1c1c;
    --ink-soft: #3a3a3a;
    --paper-light: #f4f4f4;
    --paper-shade: #dedede;
    --backdrop: #d4d4d4;
  }
  * { margin: 0; padding: 0; box-sizing: border-box; }
  html, body {
    width: 1200px; height: 780px; overflow: hidden;
    background: var(--backdrop);
    font-family: "Questrial", "Century Gothic", sans-serif;
  }
  .letterhead {
    position: absolute; left: 338px; top: 20px;
    width: 524px; height: 740px;
    background: linear-gradient(160deg, var(--paper-light) 0%, var(--paper-shade) 100%);
  }
  .corner-block {
    position: absolute; left: 437px; top: 0;
    width: 87px; height: 102px;
    background: var(--brand-red);
  }
  .corner-triangle {
    position: absolute; left: 438px; top: 111px;
    width: 86px; height: 85px;
  }
  .brand {
    position: absolute; left: 55px; top: 56px;
    display: flex; align-items: center; gap: 6px;
  }
  .brand-square {
    width: 24px; height: 24px; background: var(--brand-red);
  }
  .brand-name {
    font-size: 35px; line-height: 1; color: var(--ink);
    letter-spacing: 0.3px;
  }
  .footer-rule {
    position: absolute; left: 55px; right: 0; top: 696px;
    height: 1px; background: var(--brand-red);
  }
  .footer {
    position: absolute; left: 55px; top: 700px;
    font-size: 6.6px; line-height: 11px; color: var(--ink-soft);
    white-space: nowrap;
  }
  .company { color: var(--brand-red); font-weight: 700; }
  .sep { margin: 0 3px; }
  .contact { display: flex; align-items: center; }
  .contact-item { display: inline-flex; align-items: center; gap: 2px; }
  .icon { width: 7px; height: 7px; }
</style>
</head>
<body>
  <main class="letterhead">
    <div class="corner-block"></div>
    <svg class="corner-triangle" viewBox="0 0 86 85" aria-hidden="true">
      <polygon points="0,85 86,0 86,85" fill="var(--brand-red)"/>
    </svg>

    <header class="brand">
      <span class="brand-square"></span>
      <span class="brand-name">VULMA</span>
    </header>

    <div class="footer-rule"></div>
    <footer class="footer">
      <div class="address">
        <span class="company">VULMA Screens GmbH</span><span class="sep">|</span>Lindorferweg 14 B<span class="sep">|</span>7410 Hollendorf<span class="sep">|</span>Österreich
      </div>
      <div class="contact">
        <span class="contact-item">
          <svg class="icon" viewBox="0 0 10 10" aria-hidden="true"><path d="M2 1 L4 1 L4.6 3.2 L3.4 4 Q4.5 6 6 6.6 L6.8 5.4 L9 6 L9 8 Q8.5 9 7.5 9 Q1 8 1 2.5 Q1 1.5 2 1Z" fill="var(--brand-red)"/></svg>
          +43 (1) 482 6170
        </span>
        <span class="sep">|</span>
        <span class="contact-item">
          <svg class="icon" viewBox="0 0 10 10" aria-hidden="true"><rect x="0.5" y="2" width="9" height="6.5" fill="var(--brand-red)"/><path d="M0.8 2.3 L5 5.6 L9.2 2.3" stroke="#fff" stroke-width="0.9" fill="none"/></svg>
          office@vulmascreens.at
        </span>
        <span class="sep">|</span>
        <span class="contact-item">
          <svg class="icon" viewBox="0 0 10 10" aria-hidden="true"><circle cx="5" cy="5" r="4.5" fill="var(--brand-red)"/><path d="M1 5 H9 M5 0.8 Q2.5 5 5 9.2 M5 0.8 Q7.5 5 5 9.2" stroke="#fff" stroke-width="0.7" fill="none"/></svg>
          www.vulmascreens.at
        </span>
        <span class="sep">|</span>
        <span class="contact-item">
          <svg class="icon" viewBox="0 0 10 10" aria-hidden="true"><circle cx="5" cy="5" r="4.5" fill="var(--brand-red)"/><path d="M1 5 H9 M5 0.8 Q2.5 5 5 9.2 M5 0.8 Q7.5 5 5 9.2" stroke="#fff" stroke-width="0.7" fill="none"/></svg>
          www.vulmaemberpane.com
        </span>
      </div>
    </footer>
  </main>
</body>
</html>
```